https://copperwillowbrambleyard.org/

We would like the website to represent 19th century African American civil war soldier's letters. We would like the site colors to be nice and clean . Along with the layout, including a great landing page , blogs and introduction.

```html
<!DOCTYPE html>
<html lang="en">
<head>
<meta charset="utf-8">
<title>About – Copperwillow Brambleyard</title>
<link href="https://fonts.googleapis.com/css2?family=Libre+Baskerville&family=Montserrat:wght@400;500;600&family=Oswald:wght@500&family=Source+Sans+3:ital@1&display=swap" rel="stylesheet">
<style>
:root{
  --navy:#00236a;
  --red:#be1e2d;
  --yellow:#f2d64b;
  --ink:#1b1a40;
  --white:#ffffff;
  --heading-grey:#54595f;
  --body-grey:#7a7a7a;
  --magenta:#e21bc8;
  --dark-name:#222222;
}
*{margin:0;padding:0;box-sizing:border-box}
html,body{width:1200px;height:2488px;overflow:hidden}
body{position:relative;font-family:"Montserrat",sans-serif;background:var(--white);color:var(--white)}
.abs{position:absolute}

/* hero */
.hero-art{top:0;left:0;width:1200px;height:1268px}
.brand{top:22px;left:72px;display:flex;align-items:center;gap:12px}
.brand-dot{width:46px;height:46px;border-radius:50%;background:var(--white)}
.brand-name{font-size:22px;font-weight:600;color:var(--white);line-height:1.1;width:230px}
.main-nav{top:47px;left:845px;display:flex;gap:27px;font-size:14px}
.main-nav a{color:var(--yellow);text-decoration:none}
.hero-panel{top:140px;left:335px;width:530px;height:140px;background:rgba(40,40,40,.35)}
.hero-title{top:150px;left:0;width:1200px;text-align:center;font-size:42px;font-weight:500;color:var(--yellow)}
.hero-text{top:224px;left:349px;width:510px;font-size:13.5px;line-height:24.5px}

/* about */
.about-title{top:664px;left:120px;width:480px;text-align:center;font-family:"Libre Baskerville",serif;font-size:50px;white-space:nowrap}
.about-text{top:754px;left:121px;width:475px;font-size:13.5px;line-height:24.5px}
.about-text p+p{margin-top:20px}
.portrait{top:566px;left:791px;width:144px;height:144px;border-radius:50%;background:radial-gradient(circle at 50% 40%,#b98a74,#4a3a36 70%,#d8d8d8)}
.profile-name{top:733px;left:600px;width:530px;text-align:center;font-family:"Libre Baskerville",serif;font-size:31px;white-space:nowrap}
.profile-role{top:797px;left:600px;width:530px;text-align:center;font-size:13.5px}
.profile-mail{top:838px;left:600px;width:530px;text-align:center;font-size:13.5px;display:flex;justify-content:center;align-items:center;gap:6px}
.socials{display:flex;gap:17px}
.social{width:32px;height:32px;border-radius:50%;background:var(--yellow)}
.profile-socials{top:877px;left:750px}
.profile-text{top:926px;left:609px;width:515px;font-size:13.5px;line-height:24.5px}
.cta{top:1160px;left:967px;width:154px;height:38px;border:1px solid var(--white);display:flex;align-items:center;justify-content:center;gap:6px;font-size:13px;font-weight:500;color:var(--white)}

/* testimonials */
.testi-title{top:1350px;left:112px;width:370px;font-family:"Libre Baskerville",serif;font-size:49px;color:var(--heading-grey);white-space:nowrap}
.testi-intro{top:1435px;left:84px;width:400px;font-size:15px;line-height:25px;color:var(--body-grey)}
.testi-photo{top:1321px;left:494px;width:635px;height:226px;background:linear-gradient(120deg,#2d4a5e,#6b7f9e 55%,#c9c7c9)}
.quote{width:515px;font-family:"Source Sans 3",sans-serif;font-style:italic;font-size:15.5px;line-height:24px;color:var(--body-grey)}
.person{display:flex;align-items:center;gap:13px}
.avatar{width:76px;height:76px;border-radius:50%;border:3px solid var(--magenta);background:linear-gradient(160deg,#d9d9d9,#8a8a8a)}
.person-name{font-family:"Oswald",sans-serif;font-weight:500;font-size:21px;color:var(--dark-name);line-height:1.1}
.person-role{font-size:9.5px;letter-spacing:1.5px;color:var(--magenta)}

/* footer */
.footer-art{top:1976px;left:0;width:1200px;height:512px}
.footer-brand{top:2100px;left:0;width:1200px;display:flex;justify-content:center;align-items:center;gap:12px}
.footer-contact{top:2226px;left:0;width:1200px;display:flex;justify-content:center;gap:16px;font-size:11px;align-items:center}
.footer-contact span{display:flex;align-items:center;gap:8px}
.footer-socials{top:2298px;left:498px;gap:20px}
.footer-socials .social{width:26px;height:26px}
.footer-nav{top:2344px;left:0;width:1200px;display:flex;justify-content:center;gap:32px;font-size:14px}
.footer-nav span{display:flex;align-items:center;gap:6px}
.copyright{top:2390px;left:0;width:1200px;text-align:center;font-size:13.5px}
</style>
</head>
<body>

<svg class="abs hero-art" viewBox="0 0 1200 1268">
  <defs>
    <linearGradient id="heroShade" x1="0" y1="0" x2="1" y2="1">
      <stop offset="0" stop-color="#6e6e6e"/>
      <stop offset=".5" stop-color="#4d4d4d"/>
      <stop offset="1" stop-color="#393939"/>
    </linearGradient>
  </defs>
  <rect width="1200" height="440" fill="url(#heroShade)" role="img" aria-label="Engraved Civil War battle scene with mounted soldiers"/>
  <polygon points="0,333 600,415 1200,333 1200,428 600,538 0,428" fill="var(--red)"/>
  <polygon points="0,428 600,538 1200,428 1200,1268 0,1268" fill="var(--navy)"/>
</svg>

<header>
  <div class="abs brand"><span class="brand-dot"></span><span class="brand-name">Copperwillow Brambleyard</span></div>
  <nav class="abs main-nav"><a href="#">Home</a><a href="#">About</a><a href="#">Blog</a><a href="#">Contact</a></nav>
</header>

<div class="abs hero-panel"></div>
<h1 class="abs hero-title">About</h1>
<p class="abs hero-text">Lorem ipsum dolor sit amet, consectetur adipiscing elit. Ut elit tellus, luctus nec ullamcorper mattis, pulvinar dapibus leo.</p>

<section>
  <h2 class="abs about-title">About Blogger</h2>
  <div class="abs about-text">
    <p>Nadine Coleridge Vance is a Virginia native and Maryland-based researcher and scholar. She has received her Ph.D. in English Literature from Ashgrove State University, her M.A. in English Literature from Wrenfield University, and her B.A. in Mass Media Arts from Linmoor University. Her areas of specialization include African American Epistolary Literature, African American Civil War letters, nineteenth-century African American and American Literature, and epistolary theory.</p>
    <p>Her research focus is on letters from African American soldiers who served in the Civil War. This research delves into the nascent black nationalist identity that catalyzed black enlistment in the USCT. She most recently transcribed twenty-one letters written by Pvt. Silas Marlow, a soldier in the 102nd USCT. Her transcription work is housed alongside Pvt. Marlow’s handwritten letters at Halvern University’s Elmstead Rare Book and Manuscript Library.</p>
  </div>

  <div class="abs portrait" role="img" aria-label="Portrait photo of the blogger"></div>
  <h3 class="abs profile-name">Nadine Coleridge Vance</h3>
  <p class="abs profile-role">Researcher And Scholar</p>
  <p class="abs profile-mail">
    <svg width="14" height="11" viewBox="0 0 14 11"><rect width="14" height="11" rx="1" fill="var(--yellow)"/><path d="M1 1.5 7 6 13 1.5" stroke="var(--navy)" stroke-width="1.4" fill="none"/></svg>
    Nadine.Vance08@Mailbox.Com
  </p>
  <div class="abs socials profile-socials"><span class="social"></span><span class="social"></span><span class="social"></span><span class="social"></span><span class="social"></span></div>
  <p class="abs profile-text">As the third great granddaughter of Pvt. Elias Thornbury, who escaped enslavement from a Louisa, Virginia plantation in 1863 to join the 29th Illinois Colored Infantry, she is interested in the merging of genealogical and archival information to more deeply understand the lives of black Civil War servicemen before and after the war. She has several published articles and encyclopedia entries; has presented at various local, state, and national conferences; and has presented at local museums, research centers, and universities.</p>
  <a class="abs cta">
    <svg width="12" height="11" viewBox="0 0 12 11"><path d="M1 5.5h9M6 1.5l4 4-4 4" stroke="var(--white)" stroke-width="1.8" fill="none"/></svg>
    Check Blogs
  </a>
</section>

<section>
  <h2 class="abs testi-title">Testimonials</h2>
  <p class="abs testi-intro">Nulla consequat malesuada turpis, fringilla varius ipsum varius vel. Sed tortor arcu, finibus non lacinia et, dignissim nec sapien.</p>
  <div class="abs testi-photo" role="img" aria-label="Close-up of a hand writing a letter with a pen"></div>

  <p class="abs quote" style="top:1558px;left:84px">In pulvinar quam diam, ut elementum neque bibendum non. Sed suscipit semper bibendum iaculis ex vel turpis facilisis consectetur.</p>
  <div class="abs person" style="top:1624px;left:84px"><div class="avatar" role="img" aria-label="Reviewer photo"></div><div><div class="person-name">JANE DOE</div><div class="person-role">DESIGNER</div></div></div>

  <p class="abs quote" style="top:1558px;left:613px">Integer iaculis ex vel turpis facilisis consectetur. Mauris fringilla eros id vehicula pellentesque. Nunc eget dapibus ipsum.</p>
  <div class="abs person" style="top:1624px;left:613px"><div class="avatar" role="img" aria-label="Reviewer photo"></div><div><div class="person-name">SUSAN HEN</div><div class="person-role">DESIGNER</div></div></div>

  <p class="abs quote" style="top:1760px;left:84px">Sed mollis feugiat iaculis. Nullam sollicitudin semper dignissim. Etiam et urna lacinia, pretium mauris eget.</p>
  <div class="abs person" style="top:1826px;left:84px"><div class="avatar" role="img" aria-label="Reviewer photo" style="background:linear-gradient(160deg,#f1c9a8,#c47a4c)"></div><div><div class="person-name">INDI BERI</div><div class="person-role">DESIGNER</div></div></div>

  <p class="abs quote" style="top:1760px;left:613px">Mauris fringilla eros id vehicula pellentesque eget dapibus ipsum. Integer orci sapien, scelerisque ut gravida sed, convallis et quam.</p>
  <div class="abs person" style="top:1826px;left:613px"><div class="avatar" role="img" aria-label="Reviewer photo" style="background:linear-gradient(160deg,#5a7d86,#3b2a2e)"></div><div><div class="person-name">KINDA JANE</div><div class="person-role">DESIGNER</div></div></div>
</section>

<footer>
  <svg class="abs footer-art" viewBox="0 0 1200 512">
    <defs>
      <linearGradient id="footShade" x1="0" y1="0" x2="0" y2="1">
        <stop offset="0" stop-color="var(--ink)"/>
        <stop offset="1" stop-color="#141233"/>
      </linearGradient>
    </defs>
    <polygon points="0,116 600,2 1200,116 1200,512 0,512" fill="url(#footShade)" role="img" aria-label="Faint silhouettes of marching soldiers"/>
  </svg>
  <div class="abs footer-brand"><span class="brand-dot"></span><span class="brand-name">Copperwillow Brambleyard</span></div>
  <div class="abs footer-contact">
    <span><svg width="12" height="12" viewBox="0 0 12 12"><path d="M2 1l2.5 0 1 3-1.5 1a7 7 0 0 0 3 3l1-1.5 3 1V10a1 1 0 0 1-1 1A9 9 0 0 1 1 2a1 1 0 0 1 1-1z" fill="var(--yellow)"/></svg>+0123456789</span>
    <span><svg width="13" height="10" viewBox="0 0 14 11"><rect width="14" height="11" rx="1" fill="var(--yellow)"/><path d="M1 1.5 7 6 13 1.5" stroke="var(--ink)" stroke-width="1.4" fill="none"/></svg>Nadine.Vance08@Mailbox.Com</span>
  </div>
  <div class="abs socials footer-socials"><span class="social"></span><span class="social"></span><span class="social"></span><span class="social"></span><span class="social"></span></div>
  <nav class="abs footer-nav">
    <span><svg width="14" height="12" viewBox="0 0 14 12"><path d="M7 0 0 6h2v6h4V8h2v4h4V6h2z" fill="var(--yellow)"/></svg>Home</span>
    <span><svg width="10" height="13" viewBox="0 0 10 13"><path d="M0 0h10v13L5 9 0 13z" fill="var(--yellow)"/></svg>About</span>
    <span><svg width="12" height="12" viewBox="0 0 12 12"><rect width="12" height="12" rx="2" fill="var(--yellow)"/><rect x="3" y="3" width="6" height="2" fill="var(--ink)"/><rect x="3" y="7" width="6" height="2" fill="var(--ink)"/></svg>Blog</span>
    <span><svg width="15" height="12" viewBox="0 0 15 12"><rect width="15" height="12" rx="1" fill="var(--yellow)"/><circle cx="5" cy="5" r="2" fill="var(--ink)"/><rect x="2.5" y="8" width="5" height="2" fill="var(--ink)"/><rect x="9" y="4" width="4" height="1.5" fill="var(--ink)"/><rect x="9" y="7" width="4" height="1.5" fill="var(--ink)"/></svg>Contact</span>
  </nav>
  <p class="abs copyright">Copyright © 2020 My Blog</p>
</footer>

</body>
</html>
```